New Management Consultant needs a Stationery Design

We are in need of a full image & identity design for a management consultancy named Veroka Solutions.

Veroka Solutions is a management consulting business focusing on the mining and resources sector that specialises in Supply Chain, Integrated Planning, Operational Leadership, Health & Safety, Logistics, Accommodation & Facilities Management and Business Process Improvement.

Excerpt from Linkora Profile:

"A Senior Process Improvement Professional, specialising in logistics, with over 20 years experience with a blue chip resource company (iron ore and diamonds). Expertise in operational leadership, logistics, business process improvement and financial management. Outstanding history of successful achievements, especially in mine scheduling system design (patents certified), cost reduction and business improvement.

Senior management role key strengths include exceptional complex problem solving, contract/contractor management, logistics scheduling and the ability to implement process improvement and optimization at all stages in the business cycle."

The overall feel should be "Efficient, Dynamic, Experienced".

The design should communicate Professional, Efficient & Creative (Think outside the box)

We require:

Business Logo
Business Card
E-Business Card (send by email and Mac Contacts)
A4 Letterhead
A4 Follower page
Invoice Template (see attached)
Presentation Template (see attached - colour scheme to be used in all the design components)

ALSO NEED recommendation for standard Font ( to be compatable with MS Word) for corporate communication.

Must Have:
- LETTERHEAD must have the following details on them

Veroka Solutions
PO Box 418, Kelmore WA 6083
M 0428 561 304
E brendan.veroka@tallwire.com

BUSINESS CARD should have the following details

Brendan Holt
Director
Veroka Solutions
PO Box 418, Kelmore WA 6083
M 0428 561 304

Industry/Entity Type

Management Consulting

```html
<!DOCTYPE html>
<html lang="en">
<head>
<meta charset="utf-8">
<title>Veroka Solutions – Presentation Template</title>
<link href="https://fonts.googleapis.com/css2?family=Roboto:wght@400;500&display=swap" rel="stylesheet">
<style>
  :root {
    --board-top: #4a4a4a;
    --board-bottom: #2a2a2a;
    --sky: #37b0e6;
    --deep-blue: #1a8fc7;
    --slate: #4a86a3;
    --orange: #f5862f;
    --white: #ffffff;
    --mark-grey: #9a9a9a;
    --label-grey: #b9b9b9;
  }
  * { margin: 0; padding: 0; box-sizing: border-box; }
  html, body { width: 1200px; height: 600px; overflow: hidden; }
  body {
    position: relative;
    background: linear-gradient(180deg, var(--board-top), var(--board-bottom));
    font-family: "Roboto", Arial, sans-serif;
  }
  .brand-header {
    position: absolute;
    top: 58px;
    left: 0;
    width: 1200px;
    display: flex;
    justify-content: center;
    align-items: center;
    gap: 16px;
  }
  .brand-header .brand-square {
    width: 42px;
    height: 42px;
    background: var(--mark-grey);
  }
  .brand-header .brand-name {
    color: var(--mark-grey);
    font-size: 30px;
    font-weight: 400;
    letter-spacing: 3px;
    text-transform: uppercase;
  }
  .slide {
    position: absolute;
    top: 222px;
    width: 287px;
    height: 223px;
  }
  .slide svg { display: block; }
  .slide--intro { left: 113px; }
  .slide--body { left: 452px; }
  .slide--end { left: 786px; }
  .slide-brand {
    position: absolute;
    display: flex;
    align-items: center;
    color: var(--white);
    font-weight: 400;
  }
  .slide--intro .slide-brand {
    left: 22px;
    top: 172px;
    gap: 6px;
    font-size: 12px;
    letter-spacing: 1px;
  }
  .slide--intro .slide-brand .brand-square { width: 14px; height: 14px; }
  .slide--body .slide-brand {
    right: 12px;
    top: 204px;
    gap: 4px;
    font-size: 8px;
    letter-spacing: 0.6px;
  }
  .slide--body .slide-brand .brand-square { width: 9px; height: 9px; }
  .slide-brand .brand-square { background: var(--orange); }
  .slide-label {
    position: absolute;
    top: 508px;
    width: 287px;
    text-align: center;
    color: var(--label-grey);
    font-size: 19px;
    font-weight: 500;
    letter-spacing: 0.5px;
    word-spacing: 3px;
  }
  .slide-label--intro { left: 126px; }
  .slide-label--body { left: 452px; }
  .slide-label--end { left: 795px; }
</style>
</head>
<body>
  <header class="brand-header">
    <span class="brand-square"></span>
    <span class="brand-name">Veroka Solutions</span>
  </header>

  <section class="slide slide--intro">
    <svg width="287" height="223" viewBox="0 0 287 223">
      <rect width="287" height="223" fill="var(--sky)"/>
      <rect x="206" y="0" width="81" height="65" fill="var(--slate)"/>
      <rect x="206" y="65" width="81" height="83" fill="var(--deep-blue)"/>
      <rect x="127" y="20" width="106" height="113" fill="var(--orange)"/>
    </svg>
    <div class="slide-brand"><span class="brand-square"></span>VEROKA SOLUTIONS</div>
  </section>

  <section class="slide slide--body">
    <svg width="287" height="223" viewBox="0 0 287 223">
      <rect width="287" height="223" fill="var(--white)"/>
      <rect x="0" y="197" width="287" height="26" fill="var(--sky)"/>
      <rect x="0" y="178" width="30" height="45" fill="var(--orange)"/>
      <rect x="19" y="167" width="37" height="30" fill="var(--slate)"/>
      <rect x="30" y="197" width="26" height="26" fill="var(--deep-blue)"/>
    </svg>
    <div class="slide-brand"><span class="brand-square"></span>VEROKA</div>
  </section>

  <section class="slide slide--end">
    <svg width="287" height="223" viewBox="0 0 287 223">
      <rect width="287" height="223" fill="var(--sky)"/>
      <rect x="0" y="75" width="80" height="84" fill="var(--deep-blue)"/>
      <rect x="0" y="159" width="80" height="64" fill="var(--slate)"/>
      <rect x="54" y="91" width="105" height="113" fill="var(--orange)"/>
    </svg>
  </section>

  <p class="slide-label slide-label--intro">Introduction Slide</p>
  <p class="slide-label slide-label--body">Body Text Slide</p>
  <p class="slide-label slide-label--end">End Slide</p>
</body>
</html>
```